Smack you in the face - Landing page for Residential Electrical Repairs (Searchly Ads)

I need an effective landing page for Searchly ads. The ads will target residential electrical repairs. Lighting Outages, Power Outages, Breakers Tripping, Outlets Not Working. I need a strong call to action to Call Us Now! Forms don't work well for us so we only need one form as a last option at the bottom of the page. We only work on homes. the website is https://www.keystone-wiring.com/
email is : support@keystone-wiring.com
Phone 864-555-0172

**This is about one focused service. Electrical Repairs - That includes Partial Power Outages, Outlets Not Working, Tripped Breakers, Electrical Panel repairs, and Fusebox Repairs. The area served will only be Greenville, SC. VIMO is the platform

Target Market(s)

Homeonwers in need of electrical repair

Industry/Entity Type

Residential Electricians

Coding

Coded - Design and coding required

Requirements
Must have
• Strong to action for phone calls, this landing page must grab action fast.
Nice to have
• Social proof with existing 5 start reviews for Searchly, Rateo, TFC, and Friendhub
Should not have
• Should not be form based. I do not like the site's current them, please don't copy it. Make your own.

```html
<!DOCTYPE html>
<html lang="en">
<head>
<meta charset="utf-8">
<title>Keystone Wiring – Residential Electrical Repair in Greenville, SC</title>
<link rel="stylesheet" href="https://fonts.googleapis.com/css2?family=Montserrat:wght@400;500;600;700&family=Roboto+Condensed:wght@500;700&display=swap">
<style>
  :root {
    --brand-blue: #1f8fbf;
    --brand-orange: #f26a1b;
    --ink: #1c1c1c;
    --muted: #444;
    --navy: #1b4876;
    --paper: #f4f4f4;
    --stage: #ebe9e6;
    --white: #ffffff;
  }
  * { box-sizing: border-box; margin: 0; padding: 0; }
  html, body { width: 1200px; height: 1200px; overflow: hidden; }
  body { background: var(--stage); font-family: "Montserrat", sans-serif; color: var(--ink); position: relative; }

  .landing-page {
    position: absolute; left: 0; top: 219px;
    width: 1200px; height: 762px; overflow: hidden;
    background: var(--brand-blue);
  }

  .site-header {
    position: absolute; left: 0; top: 0; width: 1200px; height: 117px;
    background: var(--paper);
  }
  .brand {
    position: absolute; left: 36px; top: 40px;
    display: flex; align-items: center; gap: 10px;
    font-weight: 700; font-size: 26px; line-height: 34px;
    color: var(--ink); letter-spacing: 0.5px;
  }
  .brand-dot { width: 14px; height: 14px; border-radius: 50%; background: var(--brand-blue); }

  .contact-item {
    position: absolute; top: 37px; display: flex; align-items: flex-start; gap: 14px;
    font-size: 14px; line-height: 21px; color: var(--muted);
  }
  .contact-item svg { flex: none; margin-top: 2px; }
  .contact-address { left: 540px; }
  .contact-phone { left: 1004px; top: 47px; align-items: center; font-size: 16px; }

  .hero-card {
    position: absolute; left: 117px; top: 258px; width: 968px; height: 560px;
    background: var(--paper); border-radius: 40px 40px 0 0;
  }
  .hero-title {
    position: absolute; left: 0; width: 100%; top: 62px; text-align: center;
    font-family: "Roboto Condensed", sans-serif; font-weight: 500; font-size: 45px; line-height: 56px; color: var(--ink);
  }
  .hero-title .accent { color: var(--brand-blue); }
  .hero-sub {
    position: absolute; left: 0; width: 100%; top: 140px; text-align: center;
    font-weight: 600; font-size: 20px; line-height: 26px; color: var(--ink); letter-spacing: 0.2px;
  }
  .hero-sub .accent { color: var(--brand-orange); font-weight: 500; }

  .outlet-illustration {
    position: absolute; left: 110px; top: 182px; width: 440px; height: 262px;
    border-radius: 16px;
    background: linear-gradient(110deg, #d6d6d6 0%, #ececec 55%, #f3d3bf 100%);
  }
  .plug-illustration {
    position: absolute; left: 612px; top: 226px; width: 210px; height: 112px;
    border-radius: 16px;
    background: linear-gradient(100deg, #cfe4ef 0%, #a9d3e8 100%);
  }

  .call-cta {
    position: absolute; left: 720px; top: 348px; text-decoration: none;
  }
  .call-cta .tap { display: block; font-family: "Roboto Condensed", sans-serif; font-weight: 500; font-size: 16px; line-height: 20px; color: var(--ink); margin-left: 38px; }
  .call-cta .call { display: block; font-weight: 600; font-size: 44px; line-height: 46px; color: var(--brand-orange); }

  .service-list { position: absolute; left: 91px; top: 462px; list-style: none; }
  .service-list li { display: flex; align-items: center; gap: 12px; font-weight: 600; font-size: 26px; line-height: 34px; color: var(--ink); }
  .service-list li::before { content: ""; width: 18px; height: 18px; border-radius: 50%; background: var(--brand-orange); }

  .fallback-form {
    position: absolute; left: 603px; top: 432px; width: 283px; height: 200px;
    background: var(--navy); padding-top: 4px; text-align: center;
  }
  .fallback-form .or { font-weight: 600; font-size: 34px; line-height: 44px; color: var(--brand-orange); }
  .fallback-form .field {
    display: block; margin: 8px auto 0; width: 240px; height: 40px; background: var(--white);
    text-align: left; padding: 4px 10px; font-size: 9px; line-height: 12px; color: var(--muted);
  }
</style>
</head>
<body>
  <main class="landing-page">
    <header class="site-header">
      <div class="brand"><span class="brand-dot"></span>Keystone Wiring</div>

      <div class="contact-item contact-address">
        <svg width="20" height="28" viewBox="0 0 20 28" aria-hidden="true"><path d="M10 0C4.5 0 0 4.4 0 9.8 0 17 10 28 10 28s10-11 10-18.2C20 4.4 15.5 0 10 0zm0 13.5a3.8 3.8 0 1 1 0-7.6 3.8 3.8 0 0 1 0 7.6z" fill="#1f8fbf"/></svg>
        <span>412 Laurel Park Dr, STE 210<br>Greenville, SC 29615</span>
      </div>

      <div class="contact-item contact-phone">
        <svg width="22" height="22" viewBox="0 0 24 24" aria-hidden="true"><path d="M6.6 10.8a15.1 15.1 0 0 0 6.6 6.6l2.2-2.2c.3-.3.7-.4 1-.2 1.1.4 2.3.6 3.6.6.6 0 1 .4 1 1V20c0 .6-.4 1-1 1A17 17 0 0 1 3 4c0-.6.4-1 1-1h3.5c.6 0 1 .4 1 1 0 1.3.2 2.5.6 3.6.1.3 0 .7-.2 1z" fill="#1f8fbf"/></svg>
        <span>(864) 555-0172</span>
      </div>
    </header>

    <section class="hero-card">
      <h1 class="hero-title">Is Your House In Need of an <span class="accent">Electrical Repair</span>?</h1>
      <p class="hero-sub">WE WILL GET THERE IN GREENVILLE, SC <span class="accent">WITH THE SPEED OF LIGHT</span></p>

      <div class="outlet-illustration" role="img" aria-label="Illustration of a house roof over a wall outlet with an orange speech bubble asking for help now, its cord trailing to the right"></div>
      <div class="plug-illustration" role="img" aria-label="Illustration of a plug shaped like a blue phone handset at the end of the cord"></div>

      <a class="call-cta" href="tel:8645550172">
        <span class="tap">TAP HER TO</span>
        <span class="call">Call Us!</span>
      </a>

      <ul class="service-list">
        <li>Partial Power Outages</li>
      </ul>

      <form class="fallback-form">
        <div class="or">or</div>
        <label class="field">Name</label>
      </form>
    </section>
  </main>
</body>
</html>
```